Skip Bin Hire Business

We are an existing business that hire out skip bins for domestic and commercial use. We are looking for a fresh look with no colours or designs in mind.
We have 2m3 and 3m3 skip bins and 3m3 up to 24m3 walk in bins.
Visit our website for more information.
www.harbourcrate.com.au
We are going to add a photo of a 3m3 skip as this is a new product for our company and not available on our website at this stage.

Industry/Entity Type

Business

Contact Information for Business Card

Harbour Crate
9218-7046
www.harbourcrate.com.au

```html
<!DOCTYPE html>
<html lang="en">
<head>
<meta charset="utf-8">
<title>Harbour Crate – Business Card</title>
<link href="https://fonts.googleapis.com/css2?family=Open+Sans:wght@600;700&display=swap" rel="stylesheet">
<style>
  :root {
    --blue: #0a14f0;
    --ink-blue: #1212c8;
    --yellow: #ffff00;
    --pale: #ffffff;
    --edge-grey: #9a9a9a;
    --shadow: rgba(0, 0, 0, 0.45);
  }
  html, body {
    margin: 0;
    padding: 0;
    width: 1200px;
    height: 741px;
    overflow: hidden;
    background: #ffffff;
  }
  .card {
    position: relative;
    width: 1200px;
    height: 741px;
    box-sizing: border-box;
    border: 3px solid var(--edge-grey);
    background: linear-gradient(to bottom, var(--pale) 0%, var(--yellow) 100%);
    font-family: "Open Sans", Arial, sans-serif;
    overflow: hidden;
  }
  .frame {
    position: absolute;
    left: 24px;
    top: 37px;
    width: 1146px;
    height: 663px;
    border-radius: 8px;
    background: linear-gradient(to bottom,
      var(--blue) 0%, var(--blue) 14%,
      var(--yellow) 45%, var(--yellow) 55%,
      var(--blue) 86%, var(--blue) 100%);
  }
  .panel {
    position: absolute;
    left: 69px;
    top: 80px;
    width: 1058px;
    height: 572px;
    border-radius: 8px;
    background: linear-gradient(to bottom, var(--pale) 0%, #ffffb0 40%, var(--yellow) 100%);
    box-shadow: 2px 3px 5px var(--shadow), inset 0 0 3px rgba(0,0,0,0.35);
  }
  .business-name {
    position: absolute;
    left: 0;
    width: 1160px;
    top: 190px;
    margin: 0;
    text-align: center;
    font-size: 136px;
    font-weight: 700;
    line-height: 1;
    letter-spacing: 1px;
    color: var(--ink-blue);
  }
  .tagline {
    position: absolute;
    right: 240px;
    top: 330px;
    margin: 0;
    font-size: 38px;
    font-weight: 600;
    line-height: 1;
    color: var(--blue);
  }
  .contact {
    position: absolute;
    left: 96px;
    top: 525px;
    margin: 0;
    font-size: 36px;
    font-weight: 600;
    line-height: 61px;
    color: var(--blue);
  }
  .contact p { margin: 0; }
</style>
</head>
<body>
  <div class="card">
    <div class="frame"></div>
    <div class="panel"></div>
    <h1 class="business-name">Harbour Crate</h1>
    <p class="tagline">Skip Bin Hire Business</p>
    <div class="contact">
      <p class="phone">Ph 9218-7046</p>
      <p class="website">www.harbourcrate.com.au</p>
    </div>
  </div>
</body>
</html>
```